Book cover needed for Christian Non-Fiction Book

I need book cover design (eBook , Paperback, and possibly case laminate Hardcover) for use on PQL and Halvet Print.
Title: Go Forth Called
Sub-Title: Leaving Shelter and Walking in Faithful Purpose
Author: Owen Callery
Also on front cover "Forward by R. Lisel Marrow"

I like clean/simple designs. Below are links to examples of covers I like...
https://www.bookvantle.example/dp/X4821QPT7M?tag=plumwick-20&linkCode=ogi&th=1&psc=1
https://www.bookvantle.example/dp/X49KTRMWHZ?tag=plumwick-20&linkCode=ogi&th=1&psc=1
https://www.bookvantle.example/dp/X22HQC51NT?tag=plumwick-20&linkCode=ogi&th=1&psc=1
https://www.bookvantle.example/dp/X48F3WZPDR?tag=plumwick-20&linkCode=ogi&th=1&psc=1
https://www.bookvantle.example/dp/X4M7UVVCLE?tag=plumwick-20&linkCode=ogi&th=1&psc=1
https://www.bookvantle.example/dp/X2R9HNNKA6?tag=plumwick-20&linkCode=ogi&th=1&psc=1

The main idea for Go Forth Called is that God is a sending God and being "on the move" or journeying is central to God's character, and therefore God's people. I write about our hesitancy to "go," and how the Bible is full of stories about people "going" from Abraham to Jesus, to the disciples of Jesus.

The core biblical text is the Great Commission in Matthew 28:16-20, where Jesus sends out his followers, though some of them doubt.

This paragraph from the forward by R. Lisel Marrow captures the tone of the book well:
This book is a call amid the turmoil. Sacred scripture contains no shortage of narratives in which humans are pulled from their ordinary lives with an inciting incident whose stakes are high. These Biblical figures are lulled from complacency and comfort zones—and yet they are reluctant to serve because they question their ability and influence. Their lessons are relevant for us today: They, and we, are always called and sent with authority. The power of the Holy Spirit equips their “going”—and ours. It’s a sending out that looks less like mastery and more humility. It’s a sending out that is unequivocal service to others modelled in a rabbi-reformer who washed feet and touched the unclean.

I have previously published two shorter books and would be very interested in getting new covers for the old books these so that the three have a similar feel. Whichever designer I go with for "Go Forth Called" I would also want to work with on creating a "branded look" for the other two books.

Target Market(s)

Christian, Religion, Spirituality Readers

Requirements
Must have
• The front cover must have this copy...
Go Forth Called
Leaving Shelter and Walking in Faithful Purpose
Owen Callery
Forward by R. Lisel Marrow

Must be willing to do the full paperback and/or hardcover, but start with thefront cover please
Nice to have
• See attached files for some book covers I like

```html
<!DOCTYPE html>
<html lang="en">
<head>
<meta charset="utf-8">
<title>Go Forth Called — Book Cover</title>
<link rel="stylesheet" href="https://fonts.googleapis.com/css2?family=Montserrat:wght@300;400&display=swap">
<style>
  :root {
    --sky-top: #dcecbf;
    --sky-mid: #e9f7e2;
    --sky-bottom: #e6f9ef;
    --title-peach: #f5a57c;
    --subtitle-brown: #8c7662;
    --flock-violet: #6f64a3;
  }
  * { margin: 0; padding: 0; box-sizing: border-box; }
  html, body { width: 800px; height: 1200px; overflow: hidden; }
  body { font-family: "Montserrat", sans-serif; }

  .cover {
    position: relative;
    width: 800px;
    height: 1200px;
    overflow: hidden;
    background: linear-gradient(200deg, var(--sky-top) 0%, var(--sky-mid) 45%, var(--sky-bottom) 100%);
  }

  .flock {
    position: absolute;
    inset: 0;
    width: 800px;
    height: 1200px;
  }

  .title {
    position: absolute;
    top: 140px;
    left: 0;
    width: 800px;
    text-align: center;
    font-family: "Montserrat", sans-serif;
    font-weight: 300;
    font-size: 172px;
    line-height: 205px;
    letter-spacing: 4px;
    color: var(--title-peach);
    text-transform: uppercase;
  }
  .title span { display: block; }

  .subtitle {
    position: absolute;
    top: 855px;
    left: 0;
    width: 800px;
    text-align: center;
    font-family: "Montserrat", sans-serif;
    font-weight: 400;
    font-size: 21px;
    line-height: 30px;
    letter-spacing: 1.5px;
    color: var(--subtitle-brown);
    text-transform: uppercase;
  }
  .subtitle span { display: block; }

  .author {
    position: absolute;
    top: 985px;
    left: 0;
    width: 800px;
    text-align: center;
    font-family: "Montserrat", sans-serif;
    font-weight: 300;
    font-size: 38px;
    letter-spacing: 2px;
    color: var(--title-peach);
    text-transform: uppercase;
  }

  .foreword {
    position: absolute;
    top: 1048px;
    left: 0;
    width: 800px;
    text-align: center;
    font-family: "Montserrat", sans-serif;
    font-weight: 400;
    font-size: 21px;
    letter-spacing: 1.5px;
    color: var(--subtitle-brown);
    text-transform: uppercase;
  }
</style>
</head>
<body>
  <main class="cover">
    <svg class="flock" viewBox="0 0 800 1200" role="img" aria-label="Flock of violet birds scattered in flight across the sky">
      <g fill="var(--flock-violet)" opacity="0.5">
        <ellipse cx="268" cy="85" rx="30" ry="10"/>
        <ellipse cx="520" cy="190" rx="30" ry="12"/>
        <ellipse cx="205" cy="298" rx="32" ry="11"/>
        <ellipse cx="685" cy="400" rx="26" ry="11"/>
        <ellipse cx="420" cy="510" rx="28" ry="12"/>
        <ellipse cx="102" cy="630" rx="30" ry="11"/>
        <ellipse cx="720" cy="665" rx="26" ry="12"/>
        <ellipse cx="345" cy="695" rx="40" ry="11"/>
        <ellipse cx="262" cy="918" rx="32" ry="11"/>
        <ellipse cx="640" cy="972" rx="38" ry="10"/>
        <ellipse cx="278" cy="1102" rx="24" ry="10"/>
      </g>
    </svg>

    <h1 class="title">
      <span>Go</span>
      <span>Forth</span>
      <span>Called</span>
    </h1>

    <p class="subtitle">
      <span>Leaving Shelter</span>
      <span>and Walking</span>
      <span>in Faithful Purpose</span>
    </p>

    <p class="author">Owen Callery</p>
    <p class="foreword">Forward by R. Lisel Marrow</p>
  </main>
</body>
</html>
```